Quorzo Landing Page & Logo

We are building a landing page for a new blockchain-based project called Quorzo. The site should look modern and minimalistic with a very brief description of the upcoming project ("Unlock your Belmitra governance stack. Win weekly prizes and a quarterly jackpot!"), a viper logo (the animal - but can just be lettering) , and a button to subscribe for updates and early access.
Examples of similar pages:
https://pellow.finance/
https://www.trunemo.org/
https://merbisket.com/
https://k7.io/
https://www.drinnet.finance/
Target Market(s)
Crypto Users (Specifically Belmitra holders)
Coding
Coded - Design and coding required
Number of Pages Required
1 page
Look and feel
Each slider illustrates characteristics of the customer's brand and the style your logo design should communicate.

```html
<!DOCTYPE html>
<html lang="en">
<head>
<meta charset="utf-8">
<title>Quorzo</title>
<link rel="stylesheet" href="https://fonts.googleapis.com/css2?family=IBM+Plex+Sans:wght@400;500;600;700&display=swap">
<style>
:root{
  --navy:#04203f;
  --navy-band:#032a50;
  --navy-deep:#021a35;
  --green:#2fe57a;
  --white:#ffffff;
  --muted:#c9d4e3;
  --line:#1c3a5c;
}
*{margin:0;padding:0;box-sizing:border-box}
html,body{width:1200px;height:2646px;overflow:hidden}
body{background:var(--navy);color:var(--white);font-family:"IBM Plex Sans",Arial,sans-serif;position:relative}
.abs{position:absolute}
.brand{font-weight:700;color:var(--white);letter-spacing:1px;line-height:1}
.site-header .brand{left:145px;top:30px;font-size:52px}
.nav{display:flex;align-items:center;gap:28px;font-size:13px;font-weight:600;letter-spacing:.3px}
.site-header .nav{left:532px;top:46px;border-left:3px solid var(--green);padding-left:18px;height:22px}
.socials{display:flex;gap:30px}
.social{width:18px;height:18px;border-radius:50%;background:var(--white);display:block}
.site-header .socials{left:891px;top:47px}
.hero-art{left:288px;top:134px;width:677px;height:503px;border-radius:40px;
  background:radial-gradient(ellipse at 55% 50%,#1e7fd6 0%,#154f9a 30%,#0a2c5c 60%,rgba(4,32,63,0) 80%)}
.hero-plate{left:311px;top:453px;width:588px;height:132px;background:#0b2548}
.hero-title{left:311px;top:453px;width:588px;text-align:center;font-size:126px;font-weight:700;line-height:132px;letter-spacing:4px}
.section-dots{left:1109px;top:383px;display:flex;flex-direction:column;gap:12px}
.section-dots i{width:7px;height:7px;border-radius:50%;background:var(--white);display:block}
.section-dots i:first-child{background:var(--green)}
.wave{left:0;width:1200px;background:radial-gradient(ellipse at 50% 45%,rgba(47,229,122,.22) 0%,rgba(47,229,122,.08) 45%,rgba(4,32,63,0) 75%)}
.wave-top{top:640px;height:290px}
.wave-bottom{top:2150px;height:300px}
.section-title{left:0;width:1200px;text-align:center;font-weight:600;font-size:48px;line-height:1.1;letter-spacing:.5px}
.section-title em{font-style:normal;color:var(--green)}
.projects-title{top:706px}
.projects-intro{left:250px;top:795px;width:700px;text-align:center;font-size:18px;line-height:29px;color:var(--muted)}
.project-art{border-radius:30px;background:radial-gradient(ellipse at center,#2f8ee8 0%,#1c5bb0 35%,rgba(4,32,63,0) 72%)}
.project-art.one{left:246px;top:955px;width:226px;height:195px}
.project-art.two{left:719px;top:950px;width:246px;height:200px;background:radial-gradient(ellipse at center,#3aa4ee 0%,#4b4fb8 35%,rgba(4,32,63,0) 72%)}
.project-text{width:360px;text-align:center;font-size:22px;font-weight:600;line-height:32.6px;top:1169px}
.project-text.one{left:180px}
.project-text.two{left:660px}
.arrow{width:45px;height:45px;border:1.5px solid #a9b8cc;border-radius:50%;display:flex;align-items:center;justify-content:center}
.arrow.light{border-color:var(--white)}
.investors{left:0;top:1506px;width:1200px;height:325px;background:var(--navy-band)}
.investors-title{top:1553px}
.investor-logo{top:1643px;height:118px;border-radius:50%}
.subscribe-title{top:1933px;font-size:49px;line-height:54px}
.subscribe-text{left:150px;top:2055px;width:900px;text-align:center;font-size:20px;font-weight:600;line-height:29px}
.email{left:336px;top:2162px;width:327px;height:62px;border-radius:31px;background:var(--white);color:#555;font-size:15px;padding-left:33px;line-height:62px}
.subscribe-btn{left:672px;top:2162px;width:192px;height:62px;border-radius:31px;background:var(--green);color:var(--navy);font-size:21px;font-weight:700;text-align:center;line-height:62px;letter-spacing:.5px}
.site-footer .brand{left:145px;top:2488px;font-size:42px}
.site-footer .nav{left:423px;top:2498px;gap:0}
.site-footer .nav span{margin:0 22px 0 0}
.site-footer .nav .sep{margin-right:22px;font-weight:400}
.site-footer .socials{left:891px;top:2500px}
.footer-rule{left:0;top:2570px;width:1200px;height:1px;background:var(--line)}
.copyright{left:0;top:2600px;width:1200px;text-align:center;font-size:14px;color:var(--muted)}
</style>
</head>
<body>
<header class="site-header">
  <div class="abs brand">QUORZO</div>
  <nav class="abs nav"><span>HOME</span><span>ABOUT</span><span>CAREERS</span><span>CONTACT</span></nav>
  <div class="abs socials"><span class="social" aria-label="Video channel"></span><span class="social" aria-label="Video channel"></span><span class="social" aria-label="Messenger"></span><span class="social" aria-label="Call"></span></div>
</header>

<div class="abs hero-art" role="img" aria-label="Isometric glowing blue data server blocks and clouds"></div>
<div class="abs hero-plate"></div>
<h1 class="abs hero-title">QUORZO</h1>
<div class="abs section-dots"><i></i><i></i><i></i><i></i></div>

<div class="abs wave wave-top" role="img" aria-label="Green dotted particle wave"></div>
<h2 class="abs section-title projects-title">UPCOMING <em>PROJECTS</em></h2>
<p class="abs projects-intro">Lorem ipsum dolor sit amet, consectetur adipiscing elit, sed do eiusmompncididunt ut labore et dolore magna aliqua.is ipsum suspendisse ultrices gravidaisus commodo viverra maecenas accumsan lacus vel facilisis.</p>

<div class="abs project-art one" role="img" aria-label="Glowing isometric processor chip"></div>
<div class="abs project-art two" role="img" aria-label="Glowing isometric server racks"></div>
<div class="abs arrow" style="left:95px;top:1178px"><svg width="14" height="20" viewBox="0 0 14 20"><path d="M10 3 3 10l7 7" fill="none" stroke="#c9d4e3" stroke-width="2"/></svg></div>
<div class="abs arrow" style="left:1060px;top:1178px"><svg width="14" height="20" viewBox="0 0 14 20"><path d="M4 3l7 7-7 7" fill="none" stroke="#c9d4e3" stroke-width="2"/></svg></div>
<p class="abs project-text one">Lorem ipsum dol aonsectetur adipiscing elited do eiusmod tempor incididunt ut labore et dolore magna aliquuis ipsum suspendisse ultrices gravidus commodo viverra mnascum san lacus vel facilisis.</p>
<p class="abs project-text two">Sed ut perspiciatis unde omnis iste natus error sit voluptatem accusantium doloeque porro quisquam est, qui dolorem ipsum quia dolor stonsectetur adipisci velited quia non numquamremque</p>

<section class="abs investors"></section>
<h2 class="abs section-title investors-title">OUR <em>INTEVESTORS</em></h2>
<div class="abs arrow light" style="left:78px;top:1688px"><svg width="14" height="20" viewBox="0 0 14 20"><path d="M10 3 3 10l7 7" fill="none" stroke="#fff" stroke-width="2.4"/></svg></div>
<div class="abs arrow light" style="left:1076px;top:1688px"><svg width="14" height="20" viewBox="0 0 14 20"><path d="M4 3l7 7-7 7" fill="none" stroke="#fff" stroke-width="2.4"/></svg></div>
<div class="abs investor-logo" style="left:175px;width:115px;background:#1f7f78" role="img" aria-label="Teal snake mascot"></div>
<div class="abs investor-logo" style="left:336px;width:143px;background:#c9a58c" role="img" aria-label="Tan snake mascot"></div>
<div class="abs investor-logo" style="left:526px;width:157px;height:100px;top:1660px;background:#2f9a3c" role="img" aria-label="Green snake mascot"></div>
<div class="abs investor-logo" style="left:739px;width:124px;background:#7c9a2a" role="img" aria-label="Olive cobra mascot"></div>
<div class="abs investor-logo" style="left:921px;width:106px;background:#c8242a" role="img" aria-label="Red cobra mascot"></div>

<h2 class="abs section-title subscribe-title">SUBSCRIBE FOR UPDATES<br><em>AND EARLY ACCESS</em></h2>
<p class="abs subscribe-text">Lorem ipsum dolor sit amet, consectetur adipiscing elit, sed do eiusmod tempor incididunt ut labore et dolore magna aliqupsum suspendisse ultrices</p>
<div class="abs wave wave-bottom" role="img" aria-label="Green dotted particle wave"></div>
<div class="abs email">Enter Email</div>
<div class="abs subscribe-btn">SUBSCRIBE</div>

<footer class="site-footer">
  <div class="abs brand">QUORZO</div>
  <nav class="abs nav"><span>HOME</span><span class="sep">/</span><span>ABOUT</span><span class="sep">/</span><span>CAREERS</span><span class="sep">/</span><span>CONTACT</span></nav>
  <div class="abs socials"><span class="social" aria-label="Video channel"></span><span class="social" aria-label="Video channel"></span><span class="social" aria-label="Messenger"></span><span class="social" aria-label="Call"></span></div>
  <div class="abs footer-rule"></div>
  <p class="abs copyright">© 2022 Quorzo. All rights reserved | &nbsp;Privacy &nbsp;| &nbsp;Terms of Use</p>
</footer>
</body>
</html>
```